Kovalen Spinal Care and Performance

We need new business cards, something more modern, clean. On the back of the card maybe a quote. The Dr. likes, “The doctor of the future will give no medicine, but will interest his patient in the care of the human frame, in diet and in the cause and prevention of disease.” - Walter Brisby. We are open to other suggestions. We are a chiropractic office.

```html
<!DOCTYPE html>
<html lang="en">
<head>
<meta charset="utf-8">
<title>Kovalen Spinal Care and Performance – Business Card</title>
<link href="https://fonts.googleapis.com/css2?family=Lato:wght@400;700;900&display=swap" rel="stylesheet">
<style>
  :root {
    --page-bg: #e6e6e8;
    --card-bg: #ffffff;
    --purple: #7b2f8f;
    --olive: #3f4a22;
    --leaf: #8bbd2b;
    --ink: #2b2b2b;
  }
  * { box-sizing: border-box; margin: 0; padding: 0; }
  html, body {
    width: 1200px; height: 900px; overflow: hidden;
    background: var(--page-bg);
    font-family: "Lato", sans-serif;
  }
  .sheet {
    position: relative; width: 1200px; height: 900px;
  }
  .card {
    position: absolute; left: 280px;
    width: 640px; height: 366px;
    background: var(--card-bg);
    border-radius: 26px;
    box-shadow: 0 8px 24px rgba(0,0,0,0.12);
  }
  .card--back { top: 50px; }
  .card--front { top: 484px; }

  /* Back: quote */
  .quote {
    position: absolute; left: 90px; right: 70px; top: 118px;
    color: var(--olive);
    font-size: 19px; line-height: 1.35;
  }
  .quote__author {
    display: block; text-align: right;
    color: var(--purple); margin-top: 2px;
  }

  /* Front: brand */
  .brand {
    position: absolute; left: 0; right: 0; top: 70px;
    display: flex; align-items: center; justify-content: center; gap: 14px;
  }
  .brand__dot {
    width: 18px; height: 18px; border-radius: 50%;
    background: var(--leaf);
  }
  .brand__name {
    color: var(--purple);
    font-weight: 700; font-size: 26px; letter-spacing: 0.5px;
    line-height: 1.15; text-align: left;
  }

  /* Front: details row */
  .details {
    position: absolute; left: 36px; right: 36px; bottom: 40px;
    display: flex; align-items: flex-end; justify-content: space-between;
  }
  .contact { list-style: none; }
  .contact__item {
    display: flex; align-items: center; gap: 10px;
    color: var(--ink); font-size: 15px; line-height: 1.55;
  }
  .contact__icon { width: 14px; height: 14px; flex: none; }
  .divider {
    width: 1px; height: 68px; background: var(--olive);
  }
  .person { text-align: center; }
  .person__name {
    color: var(--purple); font-weight: 900; font-size: 26px; letter-spacing: 0.5px;
  }
  .person__role { color: var(--ink); font-size: 17px; }
  .address {
    color: var(--ink); font-size: 15px; line-height: 1.5; text-align: right;
  }
</style>
</head>
<body>
<main class="sheet">

  <section class="card card--back" aria-label="Card back">
    <blockquote class="quote">
      “The doctor of the future will give no medicine, but will interest his patient in the care of the human frame, in diet and in the cause and prevention of disease.”
      <cite class="quote__author">- Walter Brisby.</cite>
    </blockquote>
  </section>

  <section class="card card--front" aria-label="Card front">
    <div class="brand">
      <span class="brand__dot" aria-hidden="true"></span>
      <span class="brand__name">Kovalen<br>Spinal Care and Performance</span>
    </div>

    <div class="details">
      <ul class="contact">
        <li class="contact__item">
          <svg class="contact__icon" viewBox="0 0 24 24" aria-hidden="true"><path fill="#7b2f8f" d="M6.6 10.8a15.1 15.1 0 0 0 6.6 6.6l2.2-2.2a1 1 0 0 1 1-.25 11.4 11.4 0 0 0 3.6.57 1 1 0 0 1 1 1V20a1 1 0 0 1-1 1A17 17 0 0 1 3 4a1 1 0 0 1 1-1h3.5a1 1 0 0 1 1 1c0 1.25.2 2.45.57 3.57a1 1 0 0 1-.25 1z"/></svg>
          1234567890
        </li>
        <li class="contact__item">
          <svg class="contact__icon" viewBox="0 0 24 24" aria-hidden="true"><rect x="2" y="5" width="20" height="14" rx="1.5" fill="#7b2f8f"/><path d="M3 6l9 7 9-7" fill="none" stroke="#fff" stroke-width="1.6"/></svg>
          info@yourmail.com
        </li>
        <li class="contact__item">
          <svg class="contact__icon" viewBox="0 0 24 24" aria-hidden="true"><circle cx="12" cy="12" r="10" fill="#7b2f8f"/><g fill="none" stroke="#fff" stroke-width="1.3"><ellipse cx="12" cy="12" rx="4" ry="9"/><path d="M3 12h18M5 7.5h14M5 16.5h14"/></g></svg>
          www.yourwebsite.com
        </li>
      </ul>

      <span class="divider" aria-hidden="true"></span>

      <div class="person">
        <div class="person__name">JOHN SMITH</div>
        <div class="person__role">Founder &amp; CEO</div>
      </div>

      <span class="divider" aria-hidden="true"></span>

      <address class="address" style="font-style:normal">
        1234 First Line Address<br>
        5678 Second Line Address
      </address>
    </div>
  </section>

</main>
</body>
</html>
```